Morvex Business Card (intended for Business Card sized magnet)

Hi guys,

I would like to get a design for my business card for the restaurant. The design must be single sided as I intend to produce business card sized magnets.

The File attached must me on and I'm open for new ides

Can you please ensure that the design meets Cardowell's magnetic business card size specifications:

http://www.cardowell.example.au/custom-magnets.aspx?txi=15695&xnid=TopNav_Magnetic+Business+Cards+(linked+item)_Magnets_Marketing+Products&xnav=TopNav

Full Bleed Size (starting document size):
90 x 52 mm
1062 x 615 pixels
* Finished artwork should use the full bleed dimensions for best results.

Document Trim Size (final size after being cut):
87 x 49 mm
1028 x 579 pixels
* Please be sure to keep all text within the safe margin.

Resolution:
300 DPI

The winning design/source files need to meet these specifications.

Thanks
Updates

Hi guys, can I see more options please Thanks

```html
<!DOCTYPE html>
<html lang="en">
<head>
<meta charset="utf-8">
<title>Morvex Business Card</title>
<link rel="stylesheet" href="https://fonts.googleapis.com/css2?family=PT+Serif&family=Open+Sans:wght@300&display=swap">
<style>
  :root {
    --card-bg: #262626;
    --ink: #ffffff;
    --band-fill: #3b3b3b;
    --dot-red: #b5202e;
    --dot-teal: #1ba3bc;
    --dot-yellow: #f2b51c;
    --grill-light: #6a6a6a;
    --grill-dark: #3e3e3e;
  }
  html, body {
    margin: 0;
    padding: 0;
    overflow: hidden;
    background: var(--card-bg);
  }
  .card {
    position: relative;
    width: 1200px;
    height: 734px;
    background: var(--card-bg);
    overflow: hidden;
    color: var(--ink);
  }
  .brand-name {
    position: absolute;
    top: 52px;
    left: 0;
    width: 100%;
    margin: 0;
    text-align: center;
    font-family: "PT Serif", Georgia, serif;
    font-weight: 400;
    font-size: 112px;
    line-height: 1;
    letter-spacing: 1px;
  }
  .ornament-band {
    position: absolute;
    left: 0;
    top: 192px;
    width: 100%;
    height: 116px;
    box-sizing: border-box;
    border-top: 5px solid var(--ink);
    border-bottom: 5px solid var(--ink);
  }
  .ornament-band .pattern-area {
    position: absolute;
    left: 0;
    right: 0;
    top: 4px;
    bottom: 4px;
    background: var(--band-fill);
  }
  .tagline {
    position: absolute;
    top: 381px;
    left: 0;
    width: 100%;
    margin: 0;
    text-align: center;
    font-family: "PT Serif", Georgia, serif;
    font-weight: 400;
    font-size: 48px;
    line-height: 1;
    letter-spacing: 0.5px;
  }
  .services {
    position: absolute;
    top: 458px;
    left: 0;
    width: 100%;
    margin: 0;
    padding: 0;
    list-style: none;
    display: flex;
    justify-content: center;
    align-items: center;
    gap: 12px;
    font-family: "Open Sans", Arial, sans-serif;
    font-weight: 300;
    font-size: 33px;
    line-height: 1;
  }
  .services .dot {
    width: 12px;
    height: 12px;
    border-radius: 50%;
    display: inline-block;
  }
  .dot.red { background: var(--dot-red); }
  .dot.teal { background: var(--dot-teal); }
  .dot.yellow { background: var(--dot-yellow); }
  .grill-illustration {
    position: absolute;
    left: 387px;
    top: 546px;
    width: 425px;
    height: 188px;
    background: linear-gradient(to bottom, var(--grill-light), var(--grill-dark));
    border-radius: 40px 40px 0 0;
  }
</style>
</head>
<body>
  <main class="card">
    <h1 class="brand-name">Morvex</h1>

    <div class="ornament-band">
      <div class="pattern-area" role="img" aria-label="Band of interlaced geometric star ornaments with red, teal and yellow centres"></div>
    </div>

    <p class="tagline">Authentic Middle Eastern Restaurant</p>

    <ul class="services">
      <li class="dot red" aria-hidden="true"></li>
      <li>Lunch</li>
      <li class="dot teal" aria-hidden="true"></li>
      <li>Dinner</li>
      <li class="dot yellow" aria-hidden="true"></li>
      <li>Take away</li>
      <li class="dot red" aria-hidden="true"></li>
    </ul>

    <div class="grill-illustration" role="img" aria-label="Grey illustration of flames rising from coals on a charcoal grill"></div>
  </main>
</body>
</html>
```